依頼概要
◆概要・特徴
弊社はweb上で印刷を承る印刷通販を運営しております。
https://qorvaprint.example/
お客様が選んで使える「感染症対策ポスター」のデザイン作成をお願いいたします。

【当選内容】
複数当選(最大3点)を予定しておりますので、ご応募は1点ずつお願いいたします。
お一人様で何点でもご応募いただけます。

【デザインの要望】
・オフィス内、飲食内、旅館など様々な場所を想定しておりますので共通性・汎用性のあるデザインを宜しくお願いします。
イメージ画像を添付します。

【サイズ詳細】
作成サイズ A2トンボ付き

その他何かご不明な点がございましたら、お気軽にご質問下さい。
よろしくお願いいたします。
皆様、ご応募いただき誠にありがとうございます。
当選デザインについてはなるべくテイストが異なるものを選びたいと思っており、添付画像のような爽やかなカラフル感?も頂けると嬉しいです。
■ 選んだ理由

汎用性があるデザイン(オフィス内・飲食・etc)で清潔さがあるのをレギュラーとしながらも明るい感じのデザインも望んでおりました為、選ばせていただきました。

■ 提案者全員のお礼・コメント

大変よく出来たデザインばかりだったため、選ぶのに非常に悩んでおりました。
この度は貴重なデザインを応募頂き誠にありがとうございました。

```html
<!DOCTYPE html>
<html lang="ja">
<head>
<meta charset="utf-8">
<title>感染症対策実施中</title>
<link rel="stylesheet" href="https://fonts.googleapis.com/css2?family=Noto+Sans+JP:wght@500;700;900&display=swap">
<style>
  :root {
    --yellow: #ffe84d;
    --yellow-deep: #f7d830;
    --cyan: #44c3ef;
    --cyan-deep: #2fb0e0;
    --navy: #1d3766;
    --white: #ffffff;
    --paper: #f4f6f8;
  }
  * { margin: 0; padding: 0; box-sizing: border-box; }
  html, body { width: 849px; height: 1200px; overflow: hidden; background: var(--white); }
  body { font-family: "Noto Sans JP", sans-serif; color: var(--navy); }
  .poster { position: relative; width: 849px; height: 1200px; background: var(--white); }

  .measures {
    position: absolute; left: 30px; top: 28px;
    width: 789px; height: 762px;
    display: grid;
    grid-template-columns: repeat(3, 1fr);
    grid-template-rows: repeat(3, 1fr);
    gap: 8px;
  }
  .measure {
    display: flex; flex-direction: column; align-items: center;
    padding: 20px 16px 18px;
    text-align: center;
  }
  .measure--yellow { background: var(--yellow); }
  .measure--cyan { background: var(--cyan); }
  .measure__art {
    width: 160px; height: 140px; border-radius: 10px;
    flex: none;
  }
  .measure--yellow .measure__art { background: linear-gradient(180deg, var(--yellow-deep), #fff6a8); }
  .measure--cyan .measure__art { background: linear-gradient(180deg, var(--cyan-deep), #9fe0f6); }
  .measure__tag {
    font-size: 12px; font-weight: 700; color: var(--white);
    background: var(--navy); padding: 2px 10px; border-radius: 3px;
    margin-bottom: 6px;
  }
  .measure--distance .measure__art { height: 112px; }
  .measure__text {
    margin-top: auto;
    font-size: 19px; font-weight: 700; line-height: 1.45;
    letter-spacing: 0.02em;
  }

  .stop {
    background: var(--white);
    display: flex; flex-direction: column; align-items: center; justify-content: center;
  }
  .stop__word { font-size: 44px; font-weight: 900; letter-spacing: 0.06em; line-height: 1; }
  .stop__count { font-size: 66px; font-weight: 900; color: var(--cyan-deep); line-height: 1.15; }
  .stop__list { display: flex; gap: 6px; list-style: none; margin-top: 6px; }
  .stop__list li {
    background: var(--navy); color: var(--white);
    font-size: 14px; font-weight: 700; padding: 3px 8px; border-radius: 3px;
  }

  .notice {
    position: absolute; left: 0; top: 800px; width: 849px; height: 332px;
    text-align: center;
  }
  .notice__rays { position: absolute; left: 0; top: 0; }
  .notice__lead {
    position: absolute; left: 0; right: 0; top: 54px;
    font-size: 34px; font-weight: 900; letter-spacing: 0.04em;
  }
  .notice__code {
    position: absolute; left: 50%; top: 104px; transform: translateX(-50%);
    background: var(--navy); color: var(--white);
    font-size: 13px; font-weight: 700; padding: 1px 16px; border-radius: 10px;
  }
  .notice__title {
    position: absolute; left: 0; right: 0; top: 124px;
    font-size: 58px; font-weight: 900; letter-spacing: 0.02em; line-height: 1.3;
  }
  .notice__title-accent { color: var(--cyan-deep); }
  .notice__body {
    position: absolute; left: 0; right: 0; top: 230px;
    font-size: 19px; font-weight: 500; line-height: 1.65;
  }

  .closing {
    position: absolute; left: 0; bottom: 0; width: 849px; height: 68px;
    background: var(--cyan);
    color: var(--white);
    display: flex; align-items: center; justify-content: center;
    font-size: 22px; font-weight: 700; letter-spacing: 0.06em;
  }
</style>
</head>
<body>
<main class="poster">
  <section class="measures">
    <div class="measure measure--yellow measure--distance">
      <span class="measure__tag">ソーシャルディスタンス</span>
      <div class="measure__art" role="img" aria-label="2m離れて立つ二人の人物のイラスト"></div>
      <p class="measure__text">人と人との<br>間隔を空けましょう。</p>
    </div>
    <div class="measure measure--cyan">
      <div class="measure__art" role="img" aria-label="マスクのイラスト"></div>
      <p class="measure__text">マスクの着用に<br>ご協力ください</p>
    </div>
    <div class="measure measure--yellow">
      <div class="measure__art" role="img" aria-label="消毒液で手指を消毒するイラスト"></div>
      <p class="measure__text">手指の消毒に<br>ご協力ください</p>
    </div>
    <div class="measure measure--cyan">
      <div class="measure__art" role="img" aria-label="額で検温を受ける人物のイラスト"></div>
      <p class="measure__text">検温に<br>ご協力ください</p>
    </div>
    <div class="stop">
      <p class="stop__word">STOP</p>
      <p class="stop__count">3密</p>
      <ul class="stop__list"><li>密接</li><li>密集</li><li>密閉</li></ul>
    </div>
    <div class="measure measure--cyan">
      <div class="measure__art" role="img" aria-label="開いた窓のイラスト"></div>
      <p class="measure__text">定期的な換気を<br>行っています</p>
    </div>
    <div class="measure measure--yellow">
      <div class="measure__art" role="img" aria-label="間隔を空けて座る人のイラスト"></div>
      <p class="measure__text">間隔を空けて<br>お座りください</p>
    </div>
    <div class="measure measure--cyan">
      <div class="measure__art" role="img" aria-label="消毒スプレーで拭き掃除するイラスト"></div>
      <p class="measure__text">定期的な清掃・消毒を<br>行っています</p>
    </div>
    <div class="measure measure--yellow">
      <div class="measure__art" role="img" aria-label="入場制限を示す人物のイラスト"></div>
      <p class="measure__text">入場制限を<br>行っています</p>
    </div>
  </section>

  <section class="notice">
    <svg class="notice__rays" width="849" height="140" viewBox="0 0 849 140" aria-hidden="true">
      <g stroke="#1d3766" stroke-width="4" stroke-linecap="round">
        <line x1="200" y1="40" x2="222" y2="62"/>
        <line x1="180" y1="74" x2="210" y2="84"/>
        <line x1="178" y1="112" x2="208" y2="108"/>
        <line x1="649" y1="40" x2="627" y2="62"/>
        <line x1="669" y1="74" x2="639" y2="84"/>
        <line x1="671" y1="112" x2="641" y2="108"/>
      </g>
    </svg>
    <p class="notice__lead">新型コロナウィルス</p>
    <span class="notice__code">COVID-19</span>
    <h1 class="notice__title"><span class="notice__title-accent">感染症対策</span>実施中</h1>
    <p class="notice__body">当店は新型コロナウィルス感染症拡大防止のため、<br>上記取り組みを徹底することで対策を行っています。</p>
  </section>

  <footer class="closing">ご理解・ご協力の程よろしくお願いいたします。</footer>
</main>
</body>
</html>
```